Luxury Brand Real Estate For Sale sign

**Update** I've added some examples from the internet of other signs that have a look similar to what I would like to see. I do not want my personal name in the sign. And the word FOR SALE Does not need to be so large - it can be more subtle.
I want to create a Real Estate for sale sign for my company that will be used for luxury/higher end real estate listings. I’m sharing my business card as well as a logo with new teal color to show what we're moving towards: we’re using Teal, white, black and gold.
Hoping the sign is simple, sophisticated and eye catching.
The sign should be 24" wide by 30" tall including the company name: Harbor Crest Realty Group and our logo, office phone number 727-555-0148 and website www.hcrgexample.com the words "For Sale"
Optional to add this e-mail address info@hcrgexample.com to the sign
Target Market(s)
Luxury home buyers
Industry/Entity Type
Real Estate
Look and feel

```html
<!DOCTYPE html>
<html lang="en">
<head>
<meta charset="utf-8">
<title>Harbor Crest Realty Group – For Sale Sign</title>
<link href="https://fonts.googleapis.com/css2?family=Cinzel:wght@700&family=Montserrat:wght@500;600&family=Saira:wght@500&display=swap" rel="stylesheet">
<style>
  :root {
    --ink: #151515;
    --header-black: #1c1c1c;
    --gold: #d9a21a;
    --gold-bright: #f6bd0e;
    --gold-deep: #c98a06;
    --gold-pale: #e6dfaa;
    --teal-light: #b5f2fc;
    --teal-pale: #e6fbff;
    --teal-text: #7fe6f6;
    --white: #ffffff;
    --backdrop: #e9e9e9;
  }
  * { margin: 0; padding: 0; box-sizing: border-box; }
  html, body { width: 1200px; height: 1200px; overflow: hidden; background: var(--backdrop); }
  .sign {
    position: absolute; left: 210px; top: 112px; width: 780px; height: 976px;
    border-radius: 24px; overflow: hidden; background: var(--header-black);
  }
  .sign-header {
    position: absolute; left: 0; top: 0; width: 100%; height: 170px;
    background: linear-gradient(#2a2a2a, var(--header-black) 60%);
    display: flex; align-items: center; justify-content: center; gap: 22px;
  }
  .brand-square { width: 38px; height: 38px; border: 4px solid var(--gold); }
  .brand-name {
    font-family: "Montserrat", sans-serif; font-weight: 600; font-size: 33px;
    letter-spacing: 1px; color: var(--gold);
  }
  .gold-stripe { position: absolute; top: 170px; left: 0; width: 100%; height: 16px; background: var(--gold-bright); border-bottom: 3px solid var(--white); }
  .headline-panel {
    position: absolute; top: 186px; left: 0; width: 100%; height: 354px;
    background: linear-gradient(var(--teal-light), var(--teal-pale));
    text-align: center; font-family: "Cinzel", serif; font-weight: 700; color: var(--ink);
  }
  .headline-for { position: absolute; top: 4px; width: 100%; font-size: 198px; line-height: 1; letter-spacing: 4px; }
  .headline-sale { position: absolute; top: 166px; width: 100%; font-size: 198px; line-height: 1; letter-spacing: 6px; }
  .email-band {
    position: absolute; top: 540px; left: 0; width: 100%; height: 68px;
    background: linear-gradient(90deg, var(--gold-pale), var(--gold) 22%, var(--gold-deep) 50%, var(--gold) 78%, var(--gold-pale));
    display: flex; align-items: center; justify-content: center; gap: 10px;
    font-family: "Montserrat", sans-serif; font-weight: 500; font-size: 42px; color: var(--white);
  }
  .icon-badge { width: 46px; height: 46px; border-radius: 50%; background: var(--white); display: flex; align-items: center; justify-content: center; }
  .contact-area { position: absolute; top: 608px; left: 0; width: 100%; height: 368px; }
  .contact-curves { position: absolute; inset: 0; }
  .contact-label {
    position: absolute; top: 86px; width: 100%; display: flex; align-items: center; justify-content: center; gap: 12px;
    font-family: "Montserrat", sans-serif; font-weight: 500; font-size: 26px; color: var(--teal-text);
  }
  .contact-label::before, .contact-label::after { content: ""; width: 116px; height: 2px; background: var(--teal-text); }
  .phone {
    position: absolute; top: 128px; width: 100%; text-align: center;
    font-family: "Saira", sans-serif; font-weight: 500; font-size: 106px; line-height: 1.1; letter-spacing: 2px; color: var(--teal-text);
  }
  .website {
    position: absolute; top: 256px; left: 85px; width: 612px; height: 69px;
    border: 2px solid var(--gold); border-radius: 35px;
    display: flex; align-items: center; justify-content: center; gap: 12px;
    font-family: "Montserrat", sans-serif; font-weight: 600; font-size: 42px; color: var(--white);
  }
</style>
</head>
<body>
  <div class="sign">
    <header class="sign-header">
      <div class="brand-square"></div>
      <div class="brand-name">HARBOR CREST REALTY GROUP</div>
    </header>
    <div class="gold-stripe"></div>
    <section class="headline-panel">
      <div class="headline-for">FOR</div>
      <div class="headline-sale">SALE</div>
    </section>
    <div class="email-band">
      <span class="icon-badge">
        <svg width="26" height="20" viewBox="0 0 26 20"><rect x="1" y="1" width="24" height="18" rx="2" fill="#d9a21a"/><path d="M2 3 L13 11 L24 3" fill="none" stroke="#fff" stroke-width="2"/></svg>
      </span>
      <span>info@hcrgexample.com</span>
    </div>
    <section class="contact-area">
      <svg class="contact-curves" viewBox="0 0 780 368" preserveAspectRatio="none">
        <rect width="780" height="368" fill="#f3fdff"/>
        <path d="M0 36 Q390 10 780 36 L780 68 Q390 12 0 68 Z" fill="#d2a226"/>
        <path d="M0 68 Q390 12 780 68 L780 84 Q390 26 0 84 Z" fill="#c6f8fd"/>
        <path d="M0 84 Q390 26 780 84 L780 368 L0 368 Z" fill="#1b1b1b"/>
      </svg>
      <div class="contact-label">CONTACT US</div>
      <div class="phone">727-555-0148</div>
      <div class="website">
        <svg width="44" height="44" viewBox="0 0 44 44" fill="none" stroke="#fff" stroke-width="2.5">
          <circle cx="22" cy="22" r="19"/><ellipse cx="22" cy="22" rx="8" ry="19"/>
          <line x1="3" y1="22" x2="41" y2="22"/><path d="M6 12 H38 M6 32 H38"/>
        </svg>
        <span>www.hcrgexample.com</span>
      </div>
    </section>
  </div>
</body>
</html>
```